Business Card Design Project

Hello Designers, hope you are all aiming enjoy the weekend
I have the Business Logo (uploaded), you can alter the color which ever way you think would work,
Im looking for a simple yet striking feel, something which will stay memorable (I have uploaded 3 examples for you to flick through)
Information on the card, will just be the bare minimum,
Double Sided
Info being
i.e.
Name
Number
Website
ABN
Tobin Wexmoor
+468213579 (singapore)
+315792846 (Australia)
+729384615 (America)
www.lomevu-linkup.example
ABN 86420913
Enjoy,
Tobin
Industry/Entity Type
Business
Look and feel
Each slider illustrates characteristics of the customer's brand and the style your logo design should communicate.

```html
<!DOCTYPE html>
<html lang="en">
<head>
<meta charset="utf-8">
<title>Lomevu Linkup — Business Card</title>
<link rel="stylesheet" href="https://fonts.googleapis.com/css2?family=Alegreya:wght@400;700&display=swap">
<style>
  :root {
    --page: #ffffff;
    --card: #3b3c41;
    --card-edge: #34353a;
    --teal: #1fa3b3;
    --teal-deep: #137d8c;
    --ink: #d9d9d9;
    --ink-soft: #bfbfbf;
  }
  html, body {
    margin: 0;
    padding: 0;
    width: 1200px;
    height: 897px;
    overflow: hidden;
    background: var(--page);
  }
  .sheet {
    position: relative;
    width: 1200px;
    height: 897px;
    font-family: "Alegreya", Georgia, serif;
  }
  .card {
    position: absolute;
    top: 0;
    width: 580px;
    height: 897px;
    border-radius: 42px;
    background:
      radial-gradient(circle at 50% 40%, rgba(255,255,255,0.03), transparent 70%),
      var(--card);
    box-shadow: inset 0 0 0 1px var(--card-edge);
    overflow: hidden;
  }
  .card--front { left: 0; }
  .card--back { left: 620px; }

  .brand-mark {
    position: absolute;
    border-radius: 50%;
    background: radial-gradient(circle at 35% 35%, var(--teal), var(--teal-deep));
  }
  .card--front .brand-mark {
    width: 250px; height: 250px;
    left: 165px; top: 322px;
  }
  .card--back .brand-mark {
    width: 196px; height: 196px;
    left: 192px; top: 72px;
  }

  .brand-name {
    position: absolute;
    left: 0; right: 0;
    margin: 0;
    text-align: center;
    color: var(--teal);
    font-weight: 400;
    letter-spacing: 1px;
    white-space: nowrap;
  }
  .card--front .brand-name { top: 752px; font-size: 62px; }
  .card--back .brand-name { top: 328px; font-size: 50px; }

  .contact {
    position: absolute;
    left: 0; right: 0;
    top: 484px;
    text-align: center;
    color: var(--ink);
  }
  .contact .icon { display: block; margin: 0 auto; }
  .phones {
    list-style: none;
    margin: 8px 0 10px;
    padding: 0;
    font-size: 32px;
    line-height: 46px;
  }
  .web, .abn {
    margin: 0;
    font-size: 31px;
    font-weight: 700;
    line-height: 38px;
    color: var(--ink);
  }
  .web { margin-top: 12px; }
</style>
</head>
<body>
<main class="sheet">
  <section class="card card--front" aria-label="Card front">
    <div class="brand-mark" aria-hidden="true"></div>
    <p class="brand-name">Lomevu Linkup</p>
  </section>

  <section class="card card--back" aria-label="Card back">
    <div class="brand-mark" aria-hidden="true"></div>
    <p class="brand-name">Lomevu Linkup</p>

    <div class="contact">
      <svg class="icon icon--phone" width="40" height="40" viewBox="0 0 40 40" aria-hidden="true">
        <path d="M6 12 Q20 2 34 12 L31 17 L25 15 L24 11 Q20 9 16 11 L15 15 L9 17 Z" fill="var(--ink-soft)"/>
        <rect x="9" y="19" width="22" height="17" rx="2" fill="var(--ink-soft)"/>
        <g fill="var(--card)">
          <circle cx="14" cy="31" r="1.3"/><circle cx="18" cy="31" r="1.3"/>
          <circle cx="22" cy="31" r="1.3"/><circle cx="26" cy="31" r="1.3"/>
          <rect x="14" y="23" width="12" height="3"/>
        </g>
      </svg>
      <ul class="phones">
        <li>+468213579 (Singapore)</li>
        <li>+315792846 (Australia)</li>
        <li>+729384615 (America)</li>
      </ul>
      <svg class="icon icon--globe" width="44" height="44" viewBox="0 0 44 44" aria-hidden="true">
        <g fill="none" stroke="var(--ink-soft)" stroke-width="2">
          <circle cx="22" cy="22" r="18"/>
          <ellipse cx="22" cy="22" rx="8" ry="18"/>
          <line x1="4" y1="22" x2="40" y2="22"/>
          <path d="M7 13 H37 M7 31 H37"/>
        </g>
      </svg>
      <p class="web">www.lomevu-linkup.example</p>
      <p class="abn">ABN 86420913</p>
    </div>
  </section>
</main>
</body>
</html>
```